Australian Careers Business Needs 2 Banner Ad Design

We need a banner ad design for a new company based in Australia called Bright Sparrows. We provide career tools and insights to young professionals. Our target market is 20-30 year olds.

We would like to see designs that attract users on the site to click on the banner and sign up for a weekly newsletter. The newsletter will feature a blog, cheat sheets etc. Inspiration in their inbox!

The second banner is to attract users to sign up for a Horizon Summit. They would click on it to find out more information and then register with their email address. This convention is a 1 day workshop designed to enhance young professionals abilities to give their best at work. There will CEO insights etc.

Use of images or flash is ok. Needs to look very professional and presented in accordance to the current colour scheme in place. Visit http://www.brightsparrows-demo.com/home to understand.

Banner sizes 300 x 250.
Mandatory use of Corporate Colours required on Font.
R66 G73 B74
R242 G240 B230
R38 G128 B138

No logo necessary.

Project Deadline Extended Reason: I made an error in selecting 2 days and meant to select 5 days. Please can I amend now without the charge as its instantly after submitting the project. I am about to close out 3 existing projects and this is the second one I've just loaded today.Hence i intend to continue repeat business.Thanks,Megan Added Wednesday, April 1, 2015

Hi All,As both banners will feature on the Bright Sparrows site there is no need for a logo or hyperlink to the site.I would like to see some better images, and a bit more creative flair.Please don't use single female images as I am wanting to avoid the women in business perception. We cater to young professionals.Some suggestions for lines to utilise on the newsletter ad:Click here for weekly career tipsInvest in your career for free hereJoin the weekly conversationWeekly career tips in your inboxSign up for our weekly newsletterSome suggestions for lines to use on the horizon summit ad:Register for the Horizon Summit - Find out how to get ahead of your peersAre you a millennial climbing the corporate ladder? Find out how to rise to the topInterested in hearing from experts who recognise millennials are our future business leaders? Click here.Thanks,Megan Added Friday, April 3, 2015

Project Deadline Extended Reason: I need to extend deadline as the designs submitted are not what I was seeking. Added Saturday, April 4, 2015

Target Market(s)

20-30 years

Industry/Entity Type

Business

Font styles to use
Sans Serif

Requirements
Must have
• Please use images in the attached as options
Should not have
• NO LOGO - Its already onsite so not needed.

```html
<!DOCTYPE html>
<html lang="en">
<head>
<meta charset="utf-8">
<title>Bright Sparrows Banner Ads</title>
<link href="https://fonts.googleapis.com/css2?family=Source+Sans+3:wght@400;600;700&display=swap" rel="stylesheet">
<style>
  :root {
    --stage-dark: #141414;
    --stage-mid: #262626;
    --heading-grey: #8c8c8c;
    --brand-slate: rgb(66, 73, 74);
    --brand-cream: rgb(242, 240, 230);
    --brand-teal: rgb(38, 128, 138);
    --banner-light: #f1f0ee;
    --white: #ffffff;
  }
  * { margin: 0; padding: 0; box-sizing: border-box; }
  html, body {
    width: 1200px; height: 749px; overflow: hidden;
  }
  body {
    position: relative;
    background: radial-gradient(ellipse at 50% 40%, var(--stage-mid) 0%, var(--stage-dark) 75%);
    font-family: "Source Sans 3", "Myriad Pro", sans-serif;
  }
  .board-title {
    position: absolute; top: 126px; width: 320px;
    text-align: center; font-size: 28px; font-weight: 400;
    color: var(--heading-grey);
  }
  .board-title--newsletter { left: 218px; }
  .board-title--convention { left: 652px; }

  .banner {
    position: absolute; top: 221px; width: 300px; height: 250px;
    background: linear-gradient(135deg, var(--white) 0%, var(--banner-light) 100%);
    overflow: hidden;
  }
  .banner--newsletter { left: 234px; }
  .banner--convention { left: 670px; border-bottom: 1px solid #333; }

  .reflection {
    position: absolute; top: 471px; width: 300px; height: 30px;
    background: linear-gradient(to bottom, rgba(255,255,255,0.12), rgba(255,255,255,0));
  }
  .reflection--newsletter { left: 234px; }
  .reflection--convention { left: 670px; }

  .photo { position: absolute; display: block; }
  .photo--phone {
    left: 0; top: 0; width: 160px; height: 250px;
    background: linear-gradient(160deg, #e4d6cf 0%, #cfc8c4 40%, #2a2a2a 55%, #d9c5bb 80%, #ece9e6 100%);
  }
  .trim-guide {
    position: absolute; left: 7px; top: 6px; width: 287px; height: 239px;
    border: 1px dashed #7a7a7a;
  }
  .headline {
    position: absolute; text-align: right; color: var(--brand-slate);
  }
  .headline--newsletter {
    right: 20px; top: 17px; font-size: 16px; line-height: 25.2px;
  }
  .signup-label {
    position: absolute; right: 19px; top: 190px;
    font-size: 13px; font-weight: 700; color: var(--brand-slate);
  }
  .cta {
    position: absolute; background: var(--brand-teal); color: var(--white);
    font-weight: 400; white-space: nowrap;
  }
  .cta--newsletter {
    left: 154px; top: 212px; width: 146px; height: 20px;
    font-size: 15px; line-height: 20px; padding-left: 6px;
  }
  .convention-art { position: absolute; left: 0; top: 0; }
  .headline--convention {
    right: 17px; top: 10px; font-size: 19px; line-height: 25px;
  }
  .cta--convention {
    left: 205px; top: 214px; width: 78px; height: 21px; border-radius: 2px;
    font-size: 13px; line-height: 21px; text-align: center;
  }
</style>
</head>
<body>
  <h2 class="board-title board-title--newsletter">Newsletter Banner</h2>
  <h2 class="board-title board-title--convention">Convention Banner</h2>

  <section class="banner banner--newsletter" aria-label="Weekly newsletter banner">
    <div class="photo photo--phone" role="img" aria-label="Photo of a hand holding a smartphone showing a news page"></div>
    <div class="trim-guide"></div>
    <p class="headline headline--newsletter">Join the<br>Weekly<br>Conversation<br>Weekly Career<br>tips in your inbox</p>
    <p class="signup-label">Sign up for</p>
    <a class="cta cta--newsletter">Weekly Newsletter</a>
  </section>
  <div class="reflection reflection--newsletter"></div>

  <section class="banner banner--convention" aria-label="Horizon Summit banner">
    <svg class="convention-art" width="300" height="250" viewBox="0 0 300 250">
      <defs>
        <linearGradient id="keyboard-tones" x1="0" y1="0" x2="1" y2="1">
          <stop offset="0" stop-color="#d9dcdd"/>
          <stop offset="0.45" stop-color="#2a8fd0"/>
          <stop offset="0.7" stop-color="#c7c9ca"/>
          <stop offset="1" stop-color="#e6e6e6"/>
        </linearGradient>
      </defs>
      <path role="img" aria-label="Photo of a finger pressing a blue keyboard key"
            d="M0 0 H152 Q140 150 84 250 H0 Z" fill="url(#keyboard-tones)"/>
      <path d="M155 0 Q146 150 86 250" fill="none" stroke="var(--brand-teal)" stroke-width="9"/>
    </svg>
    <p class="headline headline--convention">Are you a<br>millennial<br>climbing the<br>corporate<br>ladder?</p>
    <a class="cta cta--convention">Click here</a>
  </section>
  <div class="reflection reflection--convention"></div>
</body>
</html>
```